New business card design

I need original, modern, business looking but dzen (minimalistic) looking design.
Also refer to websit trevanix.ru

Text is

Дробышев Кирилл, PMP
Партнер

Моб. +7 (915) 460 7185
info@trevanix.ru
Москва, Россия, 117342, ул. Береговая 7/2
=====================

Drobyshev Kirill, PMP
Partner

Mob. +7 (915) 460 7185
info@trevanix.ru
Moscow, Russia,117342, Beregovaya 7/2

Industry/Entity Type

Business

Font styles to use
Serif
Sans Serif

```html
<!DOCTYPE html>
<html lang="ru">
<head>
<meta charset="utf-8">
<title>Trevanix — визитная карточка</title>
<link rel="stylesheet" href="https://fonts.googleapis.com/css2?family=Open+Sans:wght@300;400;700&display=swap">
<style>
  :root {
    --bg: #e9e6e1;
    --card: #ffffff;
    --card-shade: #f1f1f1;
    --ink: #3a3a3a;
    --muted: #555a5e;
    --accent: #3cb8e0;
    --accent-deep: #1f8fc9;
    --rule: #d4d4d4;
  }
  * { box-sizing: border-box; margin: 0; padding: 0; }
  html, body { width: 1200px; height: 903px; overflow: hidden; }
  body {
    background: var(--bg);
    font-family: "Open Sans", Arial, sans-serif;
    color: var(--ink);
    position: relative;
  }
  .card {
    position: absolute;
    top: 296px;
    width: 540px;
    height: 310px;
    border-radius: 22px;
    background: linear-gradient(160deg, var(--card) 0%, var(--card) 55%, var(--card-shade) 100%);
    box-shadow: 0 6px 18px rgba(0,0,0,.12);
    overflow: hidden;
  }
  .card--front { left: 40px; }
  .card--back { left: 620px; }

  .brand { display: flex; align-items: center; gap: 14px; }
  .brand__mark { width: 34px; height: 34px; background: var(--accent-deep); border-radius: 4px; }
  .brand__name { font-weight: 300; color: var(--ink); letter-spacing: .5px; line-height: 1; }

  .card--front .brand { position: absolute; left: 0; right: 0; top: 120px; justify-content: center; }
  .card--front .brand__name { font-size: 56px; }
  .card--front .brand__mark { width: 46px; height: 46px; }
  .front__web { position: absolute; right: 34px; bottom: 26px; font-size: 13px; color: var(--muted); }

  .card--back .brand { position: absolute; left: 0; right: 0; top: 34px; justify-content: center; }
  .card--back .brand__name { font-size: 44px; }
  .back__rule { position: absolute; left: 270px; top: 118px; width: 1px; height: 160px; background: var(--rule); }
  .contact { position: absolute; top: 124px; width: 230px; font-size: 12px; line-height: 1.55; color: var(--muted); }
  .contact--ru { left: 24px; text-align: right; }
  .contact--en { left: 290px; text-align: left; }
  .contact__name { color: var(--accent); font-weight: 700; font-size: 14px; text-transform: uppercase; margin-bottom: 2px; }
  .contact__role { margin-bottom: 6px; }
  .contact__line { display: flex; align-items: center; gap: 7px; }
  .contact--ru .contact__line { justify-content: flex-end; }
  .icon { width: 11px; height: 11px; flex: none; }
  .icon path, .icon circle, .icon rect { fill: none; stroke: var(--accent-deep); stroke-width: 1.6; }
</style>
</head>
<body>
  <section class="card card--front">
    <div class="brand">
      <span class="brand__mark"></span>
      <span class="brand__name">Trevanix</span>
    </div>
    <p class="front__web">www.trevanix.ru</p>
  </section>

  <section class="card card--back">
    <div class="brand">
      <span class="brand__mark"></span>
      <span class="brand__name">Trevanix</span>
    </div>
    <div class="back__rule"></div>

    <div class="contact contact--ru">
      <p class="contact__name">Дробышев Кирилл, PMP</p>
      <p class="contact__role">Партнер</p>
      <p>Москва, Россия,</p>
      <p>117342, ул. Береговая 7/2</p>
      <p class="contact__line">+7 (915) 460 7185
        <svg class="icon" viewBox="0 0 12 12"><path d="M2 1.5h2.5l1 2.5-1.5 1a6 6 0 0 0 3 3l1-1.5 2.5 1V10a1 1 0 0 1-1 1A9 9 0 0 1 1 2.5a1 1 0 0 1 1-1z"/></svg></p>
      <p class="contact__line">info@trevanix.ru
        <svg class="icon" viewBox="0 0 12 12"><rect x="1" y="2.5" width="10" height="7"/><path d="M1 2.5l5 4 5-4"/></svg></p>
      <p class="contact__line">www.trevanix.ru
        <svg class="icon" viewBox="0 0 12 12"><circle cx="6" cy="6" r="5"/><path d="M1 6h10M6 1c-2.5 3-2.5 7 0 10M6 1c2.5 3 2.5 7 0 10"/></svg></p>
    </div>

    <div class="contact contact--en">
      <p class="contact__name">Drobyshev Kirill, PMP</p>
      <p class="contact__role">Partner</p>
      <p>Moscow, Russia,</p>
      <p>117342, Beregovaya 7/2</p>
      <p class="contact__line"><svg class="icon" viewBox="0 0 12 12"><path d="M2 1.5h2.5l1 2.5-1.5 1a6 6 0 0 0 3 3l1-1.5 2.5 1V10a1 1 0 0 1-1 1A9 9 0 0 1 1 2.5a1 1 0 0 1 1-1z"/></svg>+7 (915) 460 7185</p>
      <p class="contact__line"><svg class="icon" viewBox="0 0 12 12"><rect x="1" y="2.5" width="10" height="7"/><path d="M1 2.5l5 4 5-4"/></svg>info@trevanix.ru</p>
      <p class="contact__line"><svg class="icon" viewBox="0 0 12 12"><circle cx="6" cy="6" r="5"/><path d="M1 6h10M6 1c-2.5 3-2.5 7 0 10M6 1c2.5 3 2.5 7 0 10"/></svg>www.trevanix.ru</p>
    </div>
  </section>
</body>
</html>
```